Tyre Company Stationary
Stationary design
Simple
Colin Ruddock
Managing Director
Marlow's Building
582b/F/3 Oleander Road
Lusaka
Zambia
colinruddock@brenholdia.com
www.brenholdia.com
This is my AI Logo

```html
<!DOCTYPE html>
<html lang="en">
<head>
<meta charset="utf-8">
<title>Brenholdia Tyres Stationery</title>
<link href="https://fonts.googleapis.com/css2?family=Roboto:wght@400;700&display=swap" rel="stylesheet">
<style>
  :root {
    --orange: #e0661c;
    --black: #161616;
    --paper: #ffffff;
    --backdrop: #e9e9e9;
    --ink: #333333;
    --ink-soft: #777777;
  }
  * { margin: 0; padding: 0; box-sizing: border-box; }
  html, body { width: 1200px; height: 936px; overflow: hidden; }
  body {
    background: var(--backdrop);
    font-family: "Roboto", Arial, sans-serif;
    color: var(--ink);
    position: relative;
  }
  .sheet {
    position: absolute;
    background: var(--paper);
    overflow: hidden;
    box-shadow: 0 2px 6px rgba(0,0,0,.12);
  }
  .sheet > svg.art { position: absolute; inset: 0; width: 100%; height: 100%; }
  .brand {
    position: absolute;
    display: flex;
    align-items: center;
    gap: 6px;
    font-weight: 700;
    color: var(--black);
    text-transform: uppercase;
    white-space: nowrap;
  }
  .brand-dot { border-radius: 50%; background: var(--orange); flex: none; }
  .region-placeholder {
    position: absolute;
    border-radius: 45%;
    background: radial-gradient(ellipse at center, rgba(120,120,120,.16), rgba(120,120,120,.05) 60%, rgba(120,120,120,0) 75%);
  }
  .contact { position: absolute; font-size: 6px; line-height: 1.45; color: var(--ink-soft); white-space: nowrap; }
  .contact .name { color: var(--ink); font-weight: 700; }

  .letterhead { left: 178px; top: 63px; width: 393px; height: 559px; }
  .letterhead .brand { left: 22px; top: 30px; font-size: 12px; gap: 5px; }
  .letterhead .brand-dot { width: 14px; height: 14px; }
  .letterhead .region-placeholder { left: 50px; top: 160px; width: 220px; height: 230px; }
  .letterhead .contact { left: 22px; bottom: 22px; }

  .folder { left: 634px; top: 38px; width: 389px; height: 584px; }
  .folder .brand { left: 84px; top: 178px; font-size: 22px; gap: 9px; }
  .folder .brand-dot { width: 34px; height: 34px; }
  .folder .region-placeholder { left: 80px; top: 110px; width: 290px; height: 340px; }

  .card-front { left: 43px; top: 665px; width: 198px; height: 96px; }
  .card-front .brand { left: 10px; top: 12px; font-size: 7px; gap: 4px; }
  .card-front .brand-dot { width: 9px; height: 9px; }
  .card-front .contact { left: 10px; top: 48px; font-size: 5px; }

  .card-back { left: 43px; top: 781px; width: 198px; height: 94px; }
  .card-back .brand { left: 50%; top: 50%; transform: translate(-50%, -50%); font-size: 7px; gap: 4px; }
  .card-back .brand-dot { width: 14px; height: 14px; }

  .envelope-front { left: 266px; top: 672px; width: 439px; height: 203px; }
  .envelope-front .brand { left: 20px; top: 22px; font-size: 10px; gap: 5px; }
  .envelope-front .brand-dot { width: 11px; height: 11px; }
  .envelope-front .region-placeholder { left: 95px; top: 35px; width: 140px; height: 140px; }
  .envelope-front .contact { left: 20px; top: 42px; font-size: 5.5px; }

  .envelope-back { left: 738px; top: 672px; width: 432px; height: 203px; }
  .envelope-back .web {
    position: absolute; left: 0; right: 0; top: 24px;
    text-align: center; color: #fff; font-size: 10px; letter-spacing: 4px;
  }
</style>
</head>
<body>

<section class="sheet letterhead">
  <svg class="art" viewBox="0 0 392 590" preserveAspectRatio="none" aria-hidden="true">
    <path d="M392 0 H318 C405 160 400 420 280 590 H392 Z" fill="var(--orange)"/>
    <path d="M262 590 C372 450 385 270 338 130 C360 270 350 450 246 590 Z" fill="var(--black)"/>
  </svg>
  <div class="region-placeholder" role="img" aria-label="Faint continent map watermark"></div>
  <div class="brand"><span class="brand-dot"></span>Brenholdia Tyres</div>
  <div class="contact">
    <div class="name">Colin Ruddock</div>
    <div>Managing Director</div>
    <div>Marlow's Building</div>
    <div>582b/F/3 Oleander Road, Lusaka, Zambia</div>
    <div>Tel +260 211 555 014</div>
    <div>Cell +260 977 555 028</div>
    <div>colinruddock@brenholdia.com</div>
    <div>www.brenholdia.com</div>
  </div>
</section>

<section class="sheet folder">
  <svg class="art" viewBox="0 0 405 683" preserveAspectRatio="none" aria-hidden="true">
    <path d="M140 0 H405 V320 C385 160 300 45 140 0 Z" fill="var(--orange)"/>
    <path d="M0 683 V440 C40 570 120 655 210 683 Z" fill="var(--orange)"/>
    <path d="M0 360 C25 530 115 640 250 683 H215 C115 648 35 560 0 420 Z" fill="var(--black)"/>
  </svg>
  <div class="region-placeholder" role="img" aria-label="Faint continent map watermark"></div>
  <div class="brand"><span class="brand-dot"></span>Brenholdia Tyres</div>
</section>

<section class="sheet card-front">
  <svg class="art" viewBox="0 0 194 101" preserveAspectRatio="none" aria-hidden="true">
    <path d="M194 30 C170 70 140 92 100 101 H194 Z" fill="var(--orange)"/>
    <path d="M194 18 C168 62 130 90 80 101 H96 C140 90 172 65 194 34 Z" fill="var(--black)"/>
  </svg>
  <div class="brand"><span class="brand-dot"></span>Brenholdia Tyres</div>
  <div class="contact">
    <div class="name">Colin Ruddock</div>
    <div>Managing Director</div>
  </div>
</section>

<section class="sheet card-back">
  <div class="brand"><span class="brand-dot"></span>Brenholdia</div>
</section>

<section class="sheet envelope-front">
  <svg class="art" viewBox="0 0 464 223" preserveAspectRatio="none" aria-hidden="true">
    <path d="M464 0 H400 C450 60 440 160 380 223 H464 Z" fill="var(--orange)"/>
    <path d="M360 223 C425 160 440 80 415 20 C430 90 415 165 345 223 Z" fill="var(--black)"/>
  </svg>
  <div class="region-placeholder" role="img" aria-label="Faint continent map watermark"></div>
  <div class="brand"><span class="brand-dot"></span>Brenholdia Tyres</div>
  <div class="contact">
    <div>Marlow's Building</div>
    <div>582b/F/3 Oleander Road, Lusaka, Zambia</div>
  </div>
</section>

<section class="sheet envelope-back">
  <svg class="art" viewBox="0 0 423 223" preserveAspectRatio="none" aria-hidden="true">
    <path d="M0 0 H423 V72 C300 92 123 92 0 72 Z" fill="var(--orange)"/>
  </svg>
  <div class="web">www.brenholdia.com</div>
</section>

</body>
</html>
```